Nectarine Point of Sale Cards for Grocery Retail Markets

We are looking to update our Nectarine point of sale card and price card. The cards will need to be 7" x 11" with a .125 bleed - one sided. See attached for the old versions. We would like this to use photos that look like true Washington State Peaches. Here are the bullet points we would like to use: - New Crop!- Tree Ripened- Excellent FlavorNOTE: The price card just needs to have a space where a retailer can write in the sale price of the item. See attachment with the white box.

Target Market(s)

Retail market shoppers

Requirements
Must have
• Pictures of Nectarines Only

```html
<!DOCTYPE html>
<html lang="en">
<head>
<meta charset="utf-8">
<title>Washington State Peaches – Point of Sale and Price Cards</title>
<link rel="stylesheet" href="https://fonts.googleapis.com/css2?family=Cabin:wght@600;700&family=Dancing+Script:wght@700&display=swap">
<style>
  :root {
    --backdrop: #5e7072;
    --card-white: #ffffff;
    --green-light: #08a650;
    --green-dark: #00773a;
    --green-ink: #0b8a3b;
    --orange: #e2621f;
    --orange-light: #ecb564;
    --gold-light: #fbe08a;
    --gold-dark: #d9a11d;
    --peach-red: #c8322a;
    --peach-orange: #f08a3a;
    --peach-yellow: #f6c36a;
    --write-in: #ebebeb;
  }
  html, body {
    margin: 0;
    padding: 0;
    width: 1200px;
    height: 2400px;
    overflow: hidden;
    background: var(--backdrop);
  }
  .sheet { display: block; width: 1200px; height: 2400px; }
  .band-title {
    font-family: "Cabin", sans-serif;
    font-weight: 700;
    font-size: 40px;
    fill: var(--card-white);
  }
  .headline {
    font-family: "Dancing Script", cursive;
    font-weight: 700;
    font-size: 96px;
  }
  .feature-label {
    font-family: "Cabin", sans-serif;
    font-weight: 600;
    font-size: 32px;
    fill: var(--card-white);
    text-anchor: middle;
  }
  .org-name {
    font-family: "Cabin", sans-serif;
    font-weight: 700;
    font-size: 26px;
    fill: var(--green-ink);
  }
</style>
</head>
<body>
<svg class="sheet" viewBox="0 0 1200 2400" xmlns="http://www.w3.org/2000/svg">
  <defs>
    <linearGradient id="green-field" x1="0" y1="0" x2="0" y2="1">
      <stop offset="0" stop-color="var(--green-dark)"/>
      <stop offset="0.35" stop-color="var(--green-light)"/>
      <stop offset="1" stop-color="#0a9a48"/>
    </linearGradient>
    <linearGradient id="orange-band" x1="0" y1="0" x2="1" y2="0">
      <stop offset="0" stop-color="var(--orange-light)"/>
      <stop offset="0.35" stop-color="var(--orange)"/>
      <stop offset="1" stop-color="var(--orange)"/>
    </linearGradient>
    <linearGradient id="gold-type" x1="0" y1="0" x2="0" y2="1">
      <stop offset="0" stop-color="var(--gold-light)"/>
      <stop offset="1" stop-color="var(--gold-dark)"/>
    </linearGradient>
    <linearGradient id="ribbon" x1="0" y1="0" x2="0" y2="1">
      <stop offset="0" stop-color="#ee8a3c"/>
      <stop offset="1" stop-color="var(--orange)"/>
    </linearGradient>
    <linearGradient id="icon-green" x1="0" y1="0" x2="1" y2="1">
      <stop offset="0" stop-color="#3fae4a"/>
      <stop offset="1" stop-color="#14703a"/>
    </linearGradient>
    <radialGradient id="peach-tones" cx="0.6" cy="0.35" r="0.8">
      <stop offset="0" stop-color="var(--peach-red)"/>
      <stop offset="0.55" stop-color="var(--peach-orange)"/>
      <stop offset="1" stop-color="var(--peach-yellow)"/>
    </radialGradient>
    <filter id="soft-shadow" x="-10%" y="-10%" width="120%" height="130%">
      <feDropShadow dx="0" dy="4" stdDeviation="4" flood-color="#000" flood-opacity="0.3"/>
    </filter>

    <g id="feature-badge-base">
      <circle r="66" fill="var(--card-white)" stroke="#3a9d4a" stroke-width="4" stroke-dasharray="6 5"/>
      <circle r="58" fill="var(--card-white)"/>
    </g>

    <g id="icon-leaf">
      <path d="M-6,20 C-40,18 -48,-6 -44,-20 C-24,-20 -6,-6 -6,20 Z" fill="#1f6e3a"/>
      <path d="M2,22 C-2,-8 18,-30 46,-34 C48,-4 30,20 2,22 Z" fill="url(#icon-green)"/>
    </g>
    <g id="icon-trees">
      <circle cx="-14" cy="-10" r="24" fill="url(#icon-green)"/>
      <circle cx="12" cy="-18" r="24" fill="url(#icon-green)"/>
      <circle cx="-34" cy="4" r="16" fill="url(#icon-green)"/>
      <circle cx="28" cy="0" r="18" fill="url(#icon-green)"/>
      <path d="M-20,4 V28 M-20,12 L-28,4 M-20,12 L-12,4 M16,0 V28 M16,10 L8,2 M16,10 L24,2" stroke="#ffffff" stroke-width="4" fill="none"/>
      <rect x="-50" y="28" width="100" height="5" fill="#1f6e3a"/>
    </g>
    <g id="icon-thumb">
      <rect x="-38" y="-6" width="14" height="40" rx="2" fill="#1f6e3a"/>
      <path d="M-18,-4 L-2,-22 C2,-30 4,-38 10,-38 C18,-38 18,-26 14,-14 H34 C42,-14 42,-4 36,-2 C42,2 40,10 34,10 C40,14 36,22 30,22 C34,28 30,34 22,34 H-18 Z" fill="url(#icon-green)"/>
    </g>

    <g id="card-art">
      <path d="M35,30 H1037 V405 C800,455 500,490 35,410 Z" fill="url(#green-field)"/>
      <rect x="35" y="30" width="1002" height="40" fill="var(--green-dark)"/>
      <rect x="35" y="70" width="800" height="87" fill="url(#orange-band)"/>
      <text class="band-title" x="76" y="128" textLength="621" lengthAdjust="spacingAndGlyphs" filter="url(#soft-shadow)">WASHINGTON STATE PEACHES</text>
      <g role="img" aria-label="Photograph of ripe red and orange peaches with leaves in a wooden crate">
        <path d="M813,30 H1037 V405 C950,425 870,435 792,440 L662,233 Z" fill="url(#peach-tones)"/>
      </g>
      <text class="headline" x="84" y="298" textLength="746" lengthAdjust="spacingAndGlyphs" fill="url(#gold-type)" stroke="#0b5a2c" stroke-width="2" paint-order="stroke" filter="url(#soft-shadow)">Taste the Difference!</text>

      <g class="feature">
        <rect x="75" y="442" width="155" height="189" fill="url(#ribbon)"/>
        <use href="#feature-badge-base" x="152" y="447"/>
        <use href="#icon-leaf" x="152" y="447"/>
        <text class="feature-label" x="152" y="557">New</text>
        <text class="feature-label" x="152" y="596">Crop!</text>
      </g>
      <g class="feature">
        <rect x="260" y="442" width="155" height="189" fill="url(#ribbon)"/>
        <use href="#feature-badge-base" x="337" y="447"/>
        <use href="#icon-trees" x="337" y="447"/>
        <text class="feature-label" x="337" y="557">Tree</text>
        <text class="feature-label" x="337" y="596">Ripened</text>
      </g>
      <g class="feature">
        <rect x="442" y="442" width="155" height="189" fill="url(#ribbon)"/>
        <use href="#feature-badge-base" x="519" y="447"/>
        <use href="#icon-thumb" x="519" y="447"/>
        <text class="feature-label" x="519" y="557" textLength="140" lengthAdjust="spacingAndGlyphs">Excellent</text>
        <text class="feature-label" x="519" y="596">Flavor</text>
      </g>
    </g>
  </defs>

  <g class="pos-card" transform="translate(63 465)">
    <rect width="1074" height="685" fill="var(--card-white)" filter="url(#soft-shadow)"/>
    <use href="#card-art"/>
    <g class="org-signature">
      <circle cx="729" cy="582" r="44" fill="var(--orange)"/>
      <text class="org-name" x="792" y="573">Cascade Orchard</text>
      <text class="org-name" x="792" y="601">Growers Council</text>
    </g>
  </g>

  <g class="price-card" transform="translate(63 1250)">
    <rect width="1074" height="685" fill="var(--card-white)" filter="url(#soft-shadow)"/>
    <use href="#card-art"/>
    <rect x="662" y="401" width="375" height="260" fill="var(--card-white)"/>
    <g class="org-signature">
      <circle cx="729" cy="461" r="44" fill="var(--orange)"/>
      <text class="org-name" x="792" y="452">Cascade Orchard</text>
      <text class="org-name" x="792" y="480">Growers Council</text>
    </g>
    <rect class="price-write-in" x="664" y="520" width="372" height="137" fill="var(--write-in)"/>
  </g>
</svg>
</body>
</html>
```